Wholesale Plant Nursery needs 1/2 page color Ad

We need a SIMPLE/CLEAN, colorful/eye catchy ½ page ad for a magazine geared to landscape architects and designers for a garden tour that we have sponsored. We have learned people do read, so we need grip them with a simple advertisement.

This particular garden tour focuses on California Native plants. This customer base is focused on conserving water, sustainability, “going green” and not planting invasive plants.

I have attached several pictures, I understand that only a few will be used.

Beginning in 2016 the company underwent new ownership and we consolidated our growing grounds to one yard. This confused many of our customers and we want to get the word out that we are still a bright and alive company that is able to provide customers with a wide variety of healthy plants that are true to name.

Our goal of the ad is to re-introduce the company and let potential customers know the following (each can be shorten if needed):
Wholesale plant suppliers
Carry a large selection of California Natives, Grasses, Succulents and Drought Tolerant Plant Material Sales staff has over 40 years combined experience with CA native and drought tolerant plant material
Next day delivery available, small delivery minimums, free freight options (this can be eliminated if needed)
Contract growing options (would like, but can be eliminated if needed)

Logo/company name must be included (file name TVG Logo)

Contact us:
Email: sales@tavorogrowersmail.com
Fax: 415-555-0182
Phone: 415-555-0136
www.tavorogrowersmail.com

Target Market(s)

Garden/Landscape Designers and Architects

Industry/Entity Type

Landscape Gardening

Font styles to use
Serif

Colors
85acd3
0456a4
33b8a4
abd037
9bcb3c
eaf2ce
0792cd
00a990
cee9f5

Requirements
Must have
• Logo/company name must be included (file name TVG Logo)
• Specs:
• Color ad: color mode: CMYK
• Files types accepted: TIFF or PDF
• Vector graphics preferred: 300ppi minimum for rasterized text/objects
• No bleed: 7.75” wide x 5” high
Nice to have
• Clean easy to read key points about company. Fresh feel. The colors offered in the color wheel by artpitchly are too pastel. I have selected a couple of the pastel colors that may work. Maybe a mix of true blues, greens, some deeper brown, possibly some gray and the pastel?
Should not have
• Busy/cluttered ad.

```html
<!DOCTYPE html>
<html lang="en">
<head>
<meta charset="utf-8">
<title>Tavoro Growers – Half Page Ad</title>
<link href="https://fonts.googleapis.com/css2?family=Lato:wght@400;700&family=Roboto+Condensed:wght@400&family=Open+Sans:ital,wght@1,700&family=Lora:ital@1&display=swap" rel="stylesheet">
<style>
  :root {
    --page-bg: #e9e9e7;
    --white: #ffffff;
    --leaf-green: #6cbf3e;
    --ink: #1c1c1c;
    --band-dark: rgba(60, 60, 60, 0.72);
    --photo-green-dark: #3f5a3a;
    --photo-green-mid: #7b9a6c;
    --photo-sky: #dfe4e2;
  }
  * { box-sizing: border-box; margin: 0; padding: 0; }
  html, body { width: 1200px; height: 1200px; overflow: hidden; background: var(--page-bg); }

  .ad {
    position: absolute;
    left: 40px; top: 238px;
    width: 1146px; height: 740px;
    transform: scale(0.9773);
    transform-origin: top left;
    background: var(--white);
    overflow: hidden;
    box-shadow: 0 4px 14px rgba(0,0,0,0.18);
  }

  .nursery-photo {
    position: absolute; left: 0; top: 0; width: 1146px; height: 562px;
    background:
      linear-gradient(180deg, var(--photo-sky) 0%, #b7c4a8 8%, #8a9c6e 20%, #7a5a5e 26%, var(--photo-green-mid) 36%, var(--photo-green-dark) 60%, #5e7a5a 80%, #4b5f48 100%);
  }

  .shapes { position: absolute; left: 0; top: 0; }

  .headline-band {
    position: absolute; left: 133px; top: 177px; width: 850px; height: 175px;
    background: var(--band-dark);
    display: flex; align-items: center; justify-content: center;
  }
  .headline {
    font-family: "Lato", sans-serif; font-weight: 400;
    font-size: 37px; line-height: 48px; color: var(--white);
    text-align: center;
  }

  .brand {
    position: absolute; left: 28px; top: 500px;
    display: flex; align-items: center; gap: 14px;
  }
  .brand-dot { width: 58px; height: 58px; border-radius: 50%; background: var(--ink); flex: none; }
  .brand-name { font-family: "Lato", sans-serif; font-size: 25px; color: var(--ink); line-height: 1.1; }
  .brand-sub { font-family: "Lora", serif; font-style: italic; font-size: 12px; color: var(--ink); }

  .tagline {
    position: absolute; left: 22px; top: 600px;
    font-family: "Open Sans", sans-serif; font-style: italic; font-weight: 700;
    font-size: 20px; letter-spacing: 2px; color: var(--white);
  }

  .contact {
    position: absolute; left: 14px; top: 646px;
    font-family: "Roboto Condensed", sans-serif; font-size: 17.5px; line-height: 23.5px; color: var(--ink);
  }

  .feature-list {
    position: absolute; top: 649px; list-style: none;
    font-family: "Roboto Condensed", sans-serif; font-size: 21px; line-height: 29px; color: var(--ink);
  }
  .feature-list.col-a { left: 436px; }
  .feature-list.col-b { left: 801px; }
  .feature-list li { display: flex; align-items: center; gap: 10px; }
  .feature-list svg { flex: none; }

  .footer-bar { position: absolute; left: 0; bottom: 0; width: 100%; height: 18px; background: var(--leaf-green); }
</style>
</head>
<body>
  <div class="ad">
    <div class="nursery-photo" role="img" aria-label="Greenhouse rows of potted native plants, grasses and shrubs"></div>

    <svg class="shapes" width="1146" height="740" viewBox="0 0 1146 740">
      <rect x="0" y="562" width="1146" height="178" fill="#ffffff"/>
      <polygon points="0,475 385,475 360,600 0,600" fill="#ffffff"/>
      <polygon points="0,596 410,596 396,632 0,632" fill="#6cbf3e"/>

      <defs>
        <radialGradient id="bloom-yellow"><stop offset="0" stop-color="#d59a1c"/><stop offset="0.35" stop-color="#f0d42a"/><stop offset="1" stop-color="#3f5a2c"/></radialGradient>
        <radialGradient id="succulent-grey"><stop offset="0" stop-color="#b7bfae"/><stop offset="1" stop-color="#7c8a73"/></radialGradient>
        <radialGradient id="berry-pink"><stop offset="0" stop-color="#e8e4e6"/><stop offset="0.5" stop-color="#c98f9f"/><stop offset="1" stop-color="#2f4a2a"/></radialGradient>
      </defs>

      <g>
        <path d="M 553 583 A 90 90 0 0 1 643 448" fill="none" stroke="#6cbf3e" stroke-width="10"/>
        <circle cx="643" cy="538" r="86" fill="#ffffff"/>
        <circle cx="643" cy="538" r="81" fill="url(#bloom-yellow)" role="img" aria-label="Yellow native daisy flower"/>
      </g>
      <g>
        <path d="M 751 583 A 90 90 0 0 1 841 448" fill="none" stroke="#6cbf3e" stroke-width="10"/>
        <circle cx="841" cy="538" r="86" fill="#ffffff"/>
        <circle cx="841" cy="538" r="81" fill="url(#succulent-grey)" role="img" aria-label="Silvery grey succulent rosettes"/>
      </g>
      <g>
        <path d="M 951 583 A 90 90 0 0 1 1041 448" fill="none" stroke="#6cbf3e" stroke-width="10"/>
        <circle cx="1041" cy="538" r="86" fill="#ffffff"/>
        <circle cx="1041" cy="538" r="81" fill="url(#berry-pink)" role="img" aria-label="White and pink bell-shaped manzanita blossoms"/>
      </g>
    </svg>

    <div class="headline-band">
      <p class="headline">Large selection of California Natives, Grasses,<br>Succulents and Drought Tolerant Plant</p>
    </div>

    <div class="brand">
      <span class="brand-dot"></span>
      <div>
        <div class="brand-name">Tavoro Growers</div>
        <div class="brand-sub">A Redcliff Holdings, Inc. Company</div>
      </div>
    </div>

    <div class="tagline">Wholesale plant suppliers</div>

    <div class="contact">
      <p>Email: sales@tavorogrowersmail.com</p>
      <p>Phone: 415-555-0136</p>
      <p>www.tavorogrowersmail.com</p>
    </div>

    <ul class="feature-list col-a">
      <li><svg width="18" height="18" viewBox="0 0 18 18"><path d="M2 16 C2 6 8 2 16 2 C16 10 12 16 2 16 Z" fill="#6cbf3e"/><path d="M3 15 L12 6" stroke="#fff" stroke-width="1.5"/></svg>NEXT DAY DELIVERY AVAILABLE</li>
      <li><svg width="18" height="18" viewBox="0 0 18 18"><path d="M2 16 C2 6 8 2 16 2 C16 10 12 16 2 16 Z" fill="#6cbf3e"/><path d="M3 15 L12 6" stroke="#fff" stroke-width="1.5"/></svg>SMALL DELIVERY MINIMUMS</li>
    </ul>
    <ul class="feature-list col-b">
      <li><svg width="18" height="18" viewBox="0 0 18 18"><path d="M2 16 C2 6 8 2 16 2 C16 10 12 16 2 16 Z" fill="#6cbf3e"/><path d="M3 15 L12 6" stroke="#fff" stroke-width="1.5"/></svg>FREE FREIGHT OPTIONS</li>
      <li><svg width="18" height="18" viewBox="0 0 18 18"><path d="M2 16 C2 6 8 2 16 2 C16 10 12 16 2 16 Z" fill="#6cbf3e"/><path d="M3 15 L12 6" stroke="#fff" stroke-width="1.5"/></svg>CONTRACT GROWING OPTIONS</li>
    </ul>

    <div class="footer-bar"></div>
  </div>
</body>
</html>
```